New Business Card Design Project for Handyman Business

I would like to purchase a customized version of a design you have previously submitted - https://www.artvelloshowcase.com/design/58172046
I love this design!
I am hoping you can design something similar to this for our Handyman Business.
Attached is our logo and some graphics we have used.
Here is a link to the Google Doc with the content that needs to be included, https://files.quorvandel.net/document/d/e/4QZTR-8kPw2LmXn5Hb7rYcVt-qaaJsK3Df9TgNpU4WeR__LmcXaBvKpHsd2Qjn7wo4tzhgrVb41K85o3ttSTq/pub
Target Market(s)
Real Estate Agents, Home Owners and Property Managers
Industry/Entity Type
Construction/ Speciality Trade
Contact Information for Business Card
https://files.quorvandel.net/document/d/7QwRtYpL_zxkn4BvHnCdFs8TmKjWaEr2LUXPo6cxhg/edit?usp=sharing
Font styles to use
Other font styles liked:
- Ubuntu
Look and feel
Each slider illustrates characteristics of the customer's brand and the style your logo design should communicate.

```html
<!DOCTYPE html>
<html lang="en">
<head>
<meta charset="utf-8">
<title>Tidewell Business Card</title>
<link rel="stylesheet" href="https://fonts.googleapis.com/css2?family=Ubuntu:wght@400;500;700&display=swap">
<style>
  :root {
    --bg: #2a2a2c;
    --card: #1c1d1f;
    --blue: #1f7ac4;
    --green: #3fb94a;
    --orange: #e8682c;
    --white: #f2f2f2;
    --rule: #8a8a8a;
  }
  * { box-sizing: border-box; margin: 0; padding: 0; }
  html, body { width: 1200px; height: 1108px; overflow: hidden; }
  body {
    background: var(--bg);
    font-family: "Ubuntu", sans-serif;
    position: relative;
  }
  .card {
    position: absolute;
    top: 204px;
    width: 400px;
    height: 700px;
    border-radius: 22px;
    background: var(--card);
    overflow: hidden;
  }
  .card--front { left: 150px; }
  .card--back { left: 650px; }

  .brand {
    position: absolute; top: 150px; left: 0; right: 0;
    display: flex; align-items: center; justify-content: center; gap: 14px;
  }
  .brand__mark { width: 30px; height: 30px; background: var(--blue); }
  .brand__name { font-size: 58px; font-weight: 700; color: var(--green); letter-spacing: -1px; }
  .brand__tagline {
    position: absolute; top: 232px; left: 0; right: 0; text-align: center;
    color: var(--orange); font-size: 15px; letter-spacing: 4px; font-weight: 500;
  }

  .person { position: absolute; top: 340px; left: 0; right: 0; text-align: center; }
  .person__name { font-size: 38px; font-weight: 500; color: var(--blue); }
  .person__name span { color: var(--green); }
  .person__title { margin-top: 2px; font-size: 15px; color: var(--orange); }

  .rule { position: absolute; left: 70px; right: 70px; height: 1px; background: var(--rule); }
  .rule--top { top: 426px; }
  .rule--bottom { top: 540px; }

  .contact {
    position: absolute; top: 440px; left: 0; right: 0; text-align: center;
    color: var(--white); font-size: 18px; line-height: 30px;
  }

  .services {
    position: absolute; top: 566px; left: 0; right: 0; text-align: center;
    color: var(--green); font-size: 16px; font-weight: 500; letter-spacing: 0.5px;
  }
  .offer {
    position: absolute; top: 604px; left: 0; right: 0;
    display: flex; justify-content: center; align-items: center; gap: 8px;
    color: var(--orange); font-size: 17px;
  }
  .offer__dot { width: 7px; height: 7px; background: var(--green); transform: rotate(45deg); }

  .back__pattern {
    position: absolute; inset: 0;
    background: linear-gradient(225deg, #5a5b5e 0%, #36373a 35%, #1e1f21 65%, #0d0d0e 100%);
  }
  .back__brand {
    position: absolute; top: 450px; right: 40px;
    display: flex; align-items: center; gap: 10px;
  }
  .back__brand .brand__mark { width: 18px; height: 18px; }
  .back__brand .brand__name { font-size: 30px; }

  .social {
    position: absolute; top: 560px; left: 30px; right: 30px;
    display: flex; align-items: center; gap: 10px;
  }
  .social__line { flex: 1; height: 1px; background: var(--green); }
  .social__icon { width: 30px; height: 30px; border-radius: 50%; border: 2px solid var(--green); }
  .hashtag {
    position: absolute; top: 608px; left: 0; right: 0; text-align: center;
    color: var(--orange); font-size: 20px;
  }
</style>
</head>
<body>
  <section class="card card--front">
    <div class="brand">
      <span class="brand__mark"></span>
      <span class="brand__name">tidewell</span>
    </div>
    <p class="brand__tagline">HOME CARE SPECIALISTS</p>

    <div class="person">
      <h1 class="person__name">Casey <span>Moreno</span></h1>
      <p class="person__title">OWNER/ HANDYMAN</p>
    </div>
    <div class="rule rule--top"></div>
    <address class="contact" style="font-style:normal">
      (555) 014-2738<br>
      casey@tidewell-home.com<br>
      Tidewell-home.com
    </address>
    <div class="rule rule--bottom"></div>

    <p class="services">COMMERCIAL AND RESDIENTIAL HANDYMAN</p>
    <p class="offer">
      <span>Improve</span><span class="offer__dot"></span>
      <span>Repair</span><span class="offer__dot"></span>
      <span>Remodel</span><span class="offer__dot"></span>
      <span>Maintain</span>
    </p>
  </section>

  <section class="card card--back">
    <div class="back__pattern" role="img" aria-label="Embossed repeating brand pattern in graded greys"></div>
    <div class="back__brand">
      <span class="brand__mark"></span>
      <span class="brand__name">tidewell</span>
    </div>
    <div class="social">
      <span class="social__line"></span>
      <span class="social__icon"></span>
      <span class="social__icon"></span>
      <span class="social__icon"></span>
      <span class="social__icon"></span>
      <span class="social__line"></span>
    </div>
    <p class="hashtag">#TidewellHandymanServices</p>
  </section>
</body>
</html>
```